Plindy Orchards Business Card Design

My company is about Natural products made from Bees Wax, of which I am farming/raising. Products like Honey when in season, body butter, hand cream, lotions, lip balm, soap and more! All Natural, with Beeswax as the base, as it has large healing properties for moisturizing and nourishing your skin.
I would prefer lots of yellows, browns, and blacks (but am open)! I think black ink on the artwork may show up the best. But your the professionals!
The artwork is very dear to me, as my son, Warren did this in the hospital when he was diagnosed with Leukemia, of which he did not survive, at eighteen.
Is it possible to put his initials on this? WDT in light colored ink.
NO BEES, NO US! Oops! I need my name on there. Paula Vantreck and number 210-555-0147. Thank you all so much.

Hospital

Plindy Orchards
All Natural Products
Paula Vantreck
210-555-0147
PlindyOrchards@mailbrook.example

```html
<!DOCTYPE html>
<html lang="en">
<head>
<meta charset="utf-8">
<title>Plindy Orchards Business Card</title>
<link rel="stylesheet" href="https://fonts.googleapis.com/css2?family=Sorts+Mill+Goudy&family=Cinzel:wght@400;700&display=swap">
<style>
  :root {
    --page-bg: #ece8e2;
    --kraft-dark: #7a4a2e;
    --kraft-mid: #a7794f;
    --kraft-light: #e4d3b4;
    --ink-cream: #f4ead8;
    --ink-brown: #6b3b1c;
    --art-magenta: #d8386e;
    --art-orange: #f39a3c;
    --art-yellow: #f6d84a;
    --art-violet: #8e72b8;
    --art-green: #7f9a3c;
    --initials: #f6eee6;
  }
  html, body {
    margin: 0;
    width: 1200px;
    height: 1000px;
    overflow: hidden;
    background: var(--page-bg);
  }
  .canvas {
    position: relative;
    width: 1200px;
    height: 1000px;
  }
  .card {
    position: absolute;
    left: 350px;
    top: 62px;
    width: 500px;
    height: 875px;
    border-radius: 6px;
    overflow: hidden;
    background: linear-gradient(180deg, var(--kraft-dark) 0%, var(--kraft-mid) 30%, var(--kraft-light) 58%, var(--kraft-light) 100%);
    box-shadow: 0 10px 30px rgba(60, 40, 20, 0.25);
  }
  .brand {
    position: absolute;
    right: 40px;
    top: 42px;
    text-align: right;
    font-family: "Sorts Mill Goudy", Georgia, serif;
    color: var(--ink-cream);
    font-size: 92px;
    line-height: 0.86;
  }
  .tagline {
    position: absolute;
    left: 40px;
    right: 40px;
    top: 262px;
    text-align: right;
    font-family: "Cinzel", Georgia, serif;
    font-size: 25px;
    letter-spacing: 1px;
    color: var(--ink-cream);
  }
  .contact {
    position: absolute;
    left: 40px;
    right: 40px;
    top: 318px;
    font-family: "Sorts Mill Goudy", Georgia, serif;
    color: var(--ink-brown);
  }
  .contact-name {
    font-family: "Cinzel", Georgia, serif;
    font-weight: 700;
    font-size: 40px;
    margin: 0 0 10px;
  }
  .contact-line {
    font-size: 27px;
    margin: 0 0 4px;
    display: flex;
    align-items: center;
    gap: 8px;
  }
  .contact-email { font-size: 23px; }
  .phone-icon { width: 26px; height: 26px; flex: none; }
  .artwork {
    position: absolute;
    left: 0;
    top: 0;
    width: 500px;
    height: 875px;
  }
  .initials {
    position: absolute;
    right: 26px;
    bottom: 20px;
    font-family: "Sorts Mill Goudy", Georgia, serif;
    font-size: 22px;
    color: var(--initials);
    letter-spacing: 1px;
  }
</style>
</head>
<body>
<main class="canvas">
  <section class="card">
    <div class="brand">Plindy<br>Orchards</div>
    <div class="tagline">All Natural Products</div>
    <div class="contact">
      <p class="contact-name">Paula Vantreck</p>
      <p class="contact-line">
        <svg class="phone-icon" viewBox="0 0 24 24" aria-hidden="true">
          <circle cx="12" cy="12" r="11" fill="none" stroke="var(--ink-brown)" stroke-width="1.6"/>
          <path d="M8 6.5c.6-.5 1.3-.4 1.6.2l1 1.8c.3.6.1 1.1-.4 1.5l-.6.4c.6 1.4 1.6 2.5 3 3.1l.5-.6c.4-.5.9-.6 1.5-.3l1.8 1c.6.3.7 1 .2 1.6l-.8.9c-.6.6-1.5.8-2.4.4-2.9-1.3-4.9-3.4-6.1-6.3-.3-.9-.1-1.8.5-2.4z" fill="var(--ink-brown)"/>
        </svg>
        210-555-0147
      </p>
      <p class="contact-line contact-email">PlindyOrchards@mailbrook.example</p>
    </div>
    <svg class="artwork" viewBox="0 0 500 875" role="img" aria-label="Colourful painted artwork of overlapping magenta, orange, yellow, violet and green shapes">
      <defs>
        <linearGradient id="artwork-tones" x1="0" y1="0" x2="1" y2="1">
          <stop offset="0" stop-color="var(--art-green)"/>
          <stop offset="0.25" stop-color="var(--art-violet)"/>
          <stop offset="0.45" stop-color="var(--art-orange)"/>
          <stop offset="0.62" stop-color="var(--art-yellow)"/>
          <stop offset="1" stop-color="var(--art-magenta)"/>
        </linearGradient>
      </defs>
      <path d="M0 560 C 120 480, 330 470, 500 540 L 500 875 L 0 875 Z" fill="url(#artwork-tones)"/>
    </svg>
    <div class="initials">WDT</div>
  </section>
</main>
</body>
</html>
```